Business Card Design

Copperfield Lantern & Spark, Inc. (CLS), located in Memphis, TN began operating on 2003. We are a certified
minority woman-owned business that genuinely takes a vested interest in our customers. We serve utilities,
government, contractors and end user markets in electrical, water, gas and industrial supplies. Our core
competency as a distributor of electrical materials has positioned us to serve business of all size. As your supply
chain partner, we arm you with the resources you need to make your supply chain more efficient. Our team
works with your team on a daily basis to help you solve problems and achieve goals. This team approach has
helped CLS customers to succeed and we can do the same for you.

NAICS Codes:
423610 Electrical Apparatus and Equipment, Wiring Supplies, and Related Equipment Merchant
Wholesalers
423510 Metal Service Centers and Other Metal Merchant Wholesalers
423720 Plumbing and Heating Equipment and Supplies (Hydronics) Merchant Wholesalers

Certifications
MBE (KRVPQAL, State of Tennessee Up-MRX and FJW), WBE (HQOLT),
WOSB, DOT (TDOT, MDOT, ALDOT, SCDOT, NCDOT, and VDOT), LOSB,
SBE, and LSB Certified
Some of Our Products Include:
. Boxes & Covers
. Conduit & Raceway
. Fittings
. Fuses
. Lamp & Ballasts
. Lighting Controls & Timers
. Lighting Fixtures
. Personal Safety
. Pipes
. Power Distribution
. Terminations Ground & Splices
. Tools & Testers
. Wire, Cords & Cable
. Wiring Devices
. Valves

Industry/Entity Type

Business

Contact Information for Business Card

Marianne T. Holloway - President/CEO
4728 Quillon Ave., Memphis, TN 38127
901-555-0147 office, 901-555-0182 fax, 901-555-0163 cell
mtholloway@clsllc-example.com - www.clsincorp-example.com

```html
<!DOCTYPE html>
<html lang="en">
<head>
<meta charset="utf-8">
<title>Copperfield Lantern &amp; Spark, Inc. — Business Card</title>
<link rel="stylesheet" href="https://fonts.googleapis.com/css2?family=EB+Garamond:wght@500&family=Source+Sans+3:wght@400;600&display=swap">
<style>
  :root {
    --backdrop: #e9e6e1;
    --card: #ffffff;
    --ink: #141414;
    --olive: #6f7a2e;
    --icon: #6c7740;
  }
  * { box-sizing: border-box; margin: 0; padding: 0; }
  html, body { width: 1200px; height: 1000px; overflow: hidden; }
  body {
    position: relative;
    background: var(--backdrop);
    font-family: "Source Sans 3", "Segoe UI", sans-serif;
    color: var(--ink);
  }
  .card {
    position: absolute;
    left: 265px;
    width: 666px;
    height: 398px;
    background: var(--card);
    box-shadow: 0 1px 3px rgba(0,0,0,.18);
  }
  .card--front { top: 73px; }
  .card--back { top: 533px; }

  .wordmark {
    position: absolute;
    display: flex;
    align-items: center;
    gap: 12px;
    font-family: "EB Garamond", Georgia, serif;
    font-weight: 500;
    color: var(--ink);
    text-transform: uppercase;
    line-height: 1;
  }
  .wordmark__dot {
    flex: none;
    width: 14px;
    height: 14px;
    background: var(--olive);
  }
  .wordmark__name { display: block; }
  .card--front .wordmark { left: 36px; top: 76px; font-size: 31px; }
  .card--back .wordmark { left: 0; right: 0; justify-content: center; top: 150px; font-size: 42px; }
  .card--back .wordmark__dot { width: 18px; height: 18px; }

  .address {
    position: absolute;
    left: 33px;
    top: 197px;
    font-size: 16px;
    line-height: 24px;
    font-style: normal;
  }
  .contact-list {
    position: absolute;
    left: 33px;
    top: 257px;
    list-style: none;
    font-size: 16px;
    line-height: 23px;
  }
  .contact-list li { display: flex; align-items: center; gap: 9px; }
  .contact-list svg { width: 14px; height: 14px; fill: var(--icon); flex: none; }

  .person {
    position: absolute;
    right: 32px;
    top: 220px;
    text-align: right;
  }
  .person__name { font-size: 21px; font-weight: 600; color: var(--olive); line-height: 28px; }
  .person__title { font-size: 16px; line-height: 22px; }

  .web {
    position: absolute;
    left: 0; right: 0;
    top: 347px;
    text-align: center;
    font-size: 16px;
    letter-spacing: 1.6px;
  }
</style>
</head>
<body>
  <section class="card card--front">
    <div class="wordmark">
      <span class="wordmark__dot"></span>
      <span class="wordmark__name">Copperfield<br>Lantern &amp; Spark</span>
    </div>

    <address class="address">4728 Quillon Ave., Memphis,<br>TN 38127</address>

    <ul class="contact-list">
      <li><svg viewBox="0 0 14 14" aria-label="Cell"><path d="M4 1h6a1 1 0 0 1 1 1v10a1 1 0 0 1-1 1H4a1 1 0 0 1-1-1V2a1 1 0 0 1 1-1zm0 2v6h6V3z"/></svg>901-555-0163</li>
      <li><svg viewBox="0 0 14 14" aria-label="Office"><path d="M1 5c0-2 3-3 6-3s6 1 6 3v1h-3V5H4v1H1zm2 2h8l1 5H2z"/></svg>901-555-0147</li>
      <li><svg viewBox="0 0 14 14" aria-label="Fax"><path d="M4 1h6v3H4zM1 5h12v6h-2V9H3v2H1zm3 5h6v3H4z"/></svg>901-555-0182</li>
      <li><svg viewBox="0 0 14 14" aria-label="Email"><path d="M1 3h12v8H1zm1 1v.5l5 3.5 5-3.5V4z"/></svg>mtholloway@clsllc-example.com</li>
      <li><svg viewBox="0 0 14 14" aria-label="Website"><path d="M7 1a6 6 0 1 0 0 12A6 6 0 0 0 7 1zm0 2a4 4 0 0 1 3.5 2H8L7 7l1.5 2L7 11a4 4 0 0 1-1-7.9z"/></svg>www.clsincorp-example.com</li>
    </ul>

    <div class="person">
      <p class="person__name">Marianne T. Holloway</p>
      <p class="person__title">President / CEO</p>
    </div>
  </section>

  <section class="card card--back">
    <div class="wordmark">
      <span class="wordmark__dot"></span>
      <span class="wordmark__name">Copperfield<br>Lantern &amp; Spark</span>
    </div>
    <p class="web">www.clsincorp-example.com</p>
  </section>
</body>
</html>
```